Label for water can - new packaging of luxury Velmora Springs water

We create water can - handy disposable metal packaging that can be closed with a cap and used for a long time. We want to stand out, look different from typical other water brands.

It is a product that the clients impulsively buys because the design attracts them. They want to take it out of their bag, they want to give it to their clients. They want to have the CAN with them all the time.

The packaging is great for kids, but we don't design product for kids. We create a tasteful luxury UNISEX design for parents who want to buy it for themselves and give it to their children at the same time.

The client will buy our product for the first time because of the design and type of packaging, the taste will make him a loyal client.

Most of water brands are generally tuned in white-blue style.

They all use images of nature, water.

We want to be different.

We are angelic water.

Minimalism describes us.

An important part of the Velmora Springs concept is wood (our glass barrel comes in a wooden case).

Our clients like gold and silver color.

The product name is CAN. And that word has a double meaning.
WATER CAN MAKE YOU HAPPY…
WATER CAN HELP YOU…
WATER CAN ENRICHE YOU…
We will play with it in future communication.

Target Market(s)

Luxury water bevarage

Font styles to use
Other font styles liked:
• Seravek, Gotham, Playfair Display

Colors
0094D4
00A9DD
6FCCEA
C7EBF8
E9F6FB

Requirements
Must have
• Packaging supports impulsive shopping, is untraditional and unisex
Should not have
• Elements traditional for water packaging

```html
<!DOCTYPE html>
<html lang="en">
<head>
<meta charset="utf-8">
<title>Velmora Springs CAN label</title>
<link rel="stylesheet" href="https://fonts.googleapis.com/css2?family=Open+Sans:wght@300;400;800&display=swap">
<style>
  :root {
    --page: #ffffff;
    --silver-light: #f4f5f6;
    --silver-mid: #d9dcdf;
    --silver-dark: #b9bdc1;
    --brand-grey: #4a5058;
    --wave-light: #9fd8f2;
    --blue-top: #4aa3df;
    --blue-mid: #2f7fca;
    --blue-deep: #2450a4;
    --white: #ffffff;
  }
  * { margin: 0; padding: 0; box-sizing: border-box; }
  html, body {
    width: 973px;
    height: 1200px;
    overflow: hidden;
    background: var(--page);
    font-family: "Open Sans", Arial, sans-serif;
  }
  .canvas {
    position: relative;
    width: 973px;
    height: 1200px;
  }
  .label {
    position: absolute;
    left: 106px;
    top: 45px;
    width: 760px;
    height: 1110px;
    overflow: hidden;
    background: linear-gradient(90deg, var(--silver-dark) 0%, var(--silver-light) 35%, var(--silver-mid) 70%, var(--silver-dark) 100%);
  }
  .wave-area {
    position: absolute;
    left: 0;
    top: 250px;
    width: 760px;
    height: 170px;
    background: linear-gradient(180deg, rgba(159, 216, 242, 0) 0%, var(--wave-light) 45%, var(--blue-top) 100%);
  }
  .blue-body {
    position: absolute;
    left: 0;
    top: 420px;
    width: 760px;
    height: 690px;
    background: linear-gradient(180deg, var(--blue-top) 0%, var(--blue-mid) 50%, var(--blue-deep) 100%);
  }
  .brand {
    position: absolute;
    left: 0;
    right: 0;
    top: 112px;
    text-align: center;
    font-weight: 300;
    font-size: 74px;
    line-height: 1.2;
    letter-spacing: -1px;
    color: var(--brand-grey);
  }
  .product-name {
    position: absolute;
    left: 168px;
    top: 430px;
    font-weight: 800;
    font-size: 155px;
    line-height: 1;
    color: var(--white);
    letter-spacing: 2px;
  }
  .features {
    position: absolute;
    left: 194px;
    top: 632px;
    list-style: none;
  }
  .feature {
    display: flex;
    align-items: center;
    height: 64px;
    margin-bottom: 27px;
    color: var(--white);
    font-size: 32px;
    font-weight: 400;
  }
  .feature:nth-child(3) { margin-bottom: 42px; }
  .feature-mark {
    width: 60px;
    height: 60px;
    margin-right: 40px;
    flex: none;
    border: 2px solid var(--white);
    border-radius: 50%;
  }
  .availability {
    position: absolute;
    left: 0;
    right: 0;
    top: 1030px;
    text-align: center;
    color: var(--white);
    font-size: 18px;
    font-weight: 400;
    opacity: 0.9;
  }
</style>
</head>
<body>
<div class="canvas">
  <section class="label">
    <div class="wave-area" role="img" aria-label="Flowing water wave graphic across the label"></div>
    <div class="blue-body"></div>

    <h1 class="brand">Velmora Springs</h1>
    <div class="product-name">CAN</div>

    <ul class="features">
      <li class="feature"><span class="feature-mark" aria-hidden="true"></span>Alkaline ph</li>
      <li class="feature"><span class="feature-mark" aria-hidden="true"></span>Low in minerals</li>
      <li class="feature"><span class="feature-mark" aria-hidden="true"></span>Icelandic glacier water</li>
      <li class="feature"><span class="feature-mark" aria-hidden="true"></span>Still</li>
    </ul>

    <p class="availability">We are available online in glass barrels for your home</p>
  </section>
</div>
</body>
</html>
```